Create for us a Shop-Stopper Business Card

We need a standout, first class business card to go along with our new brand strategy. Sleek, Contemporary and fresh.

Colors and theme must sync with our websitewww.pelvorpower.co.uk

We want a business card that has a global brand appeal. TKR Energy is a small UK renewable company that specialises in energy projects in Africa. We want a business card that has the following characteristics: Very short, precise, global, stand out, NOT TOO LOUD but contemporary. The company's colour themes are White, Grey with a hint of green.

Target Market(s)

Business exec, high net worth individuals, investors, commercial leaders, suppliers, government officials

Industry/Entity Type

Solar Energy

Contact Information for Business Card

Logo, Name, Title, Address, web address, email,

Requirements
Must have
• Logo must be sharp
Nice to have
• Adapt fonts from the logo. The large circular side of the logo at the back in a very refreshing way
Should not have
• No solar panel shapes or image.Very little black. If possible avoid black. Its not coming out nice. I think !!!

```html
<!DOCTYPE html>
<html lang="en">
<head>
<meta charset="utf-8">
<title>TKR Energy – Business Card</title>
<link rel="stylesheet" href="https://fonts.googleapis.com/css2?family=Nunito+Sans:wght@400;600;700;800&display=swap">
<style>
  :root {
    --backdrop: #2f3336;
    --card-white: #ffffff;
    --card-grey: #e4e5e7;
    --ink: #1c1d1f;
    --ink-soft: #2a2b2d;
    --green: #1f8f3a;
    --green-deep: #0a8a3c;
    --green-light: #8acd45;
    --faint-ring: rgba(0, 0, 0, 0.045);
  }
  * { margin: 0; padding: 0; box-sizing: border-box; }
  html, body { width: 1200px; height: 661px; overflow: hidden; }
  body {
    background: var(--backdrop);
    font-family: "Nunito Sans", Arial, sans-serif;
    position: relative;
  }
  .card {
    position: absolute;
    top: 153px;
    height: 348px;
    overflow: hidden;
  }
  /* Front */
  .card-front {
    left: 24px;
    width: 568px;
    background: linear-gradient(135deg, var(--card-white) 0%, #f4f4f5 45%, var(--card-grey) 100%);
  }
  .front-ring {
    position: absolute;
    left: 355px;
    top: -5px;
    width: 250px;
    height: 250px;
    border-radius: 50%;
    border: 34px solid var(--faint-ring);
  }
  .holder-name {
    position: absolute;
    left: 34px;
    top: 30px;
    font-size: 18px;
    font-weight: 700;
    color: var(--ink);
  }
  .holder-title {
    position: absolute;
    left: 34px;
    top: 55px;
    font-size: 16px;
    color: var(--ink-soft);
  }
  .brand-strip {
    position: absolute;
    left: 0;
    top: 237px;
    width: 21px;
    height: 21px;
    background: var(--green);
  }
  .brand-mark {
    position: absolute;
    left: 32px;
    top: 220px;
    width: 54px;
    height: 54px;
    border-radius: 50%;
    background: var(--green);
  }
  .brand-name {
    position: absolute;
    left: 94px;
    top: 226px;
    font-size: 30px;
    font-weight: 700;
    letter-spacing: 0.5px;
    line-height: 40px;
    color: var(--ink-soft);
  }
  .tagline-band {
    position: absolute;
    left: 314px;
    top: 236px;
    width: 254px;
    height: 23px;
    background: var(--green);
    color: var(--card-white);
    font-size: 16px;
    font-weight: 700;
    line-height: 23px;
    padding-left: 15px;
  }
  .contact {
    position: absolute;
    left: 34px;
    top: 282px;
    font-size: 15.5px;
    line-height: 22px;
    color: var(--ink-soft);
  }
  /* Back */
  .card-back {
    left: 610px;
    width: 571px;
    background: linear-gradient(40deg, var(--green-deep) 0%, #3aa845 50%, var(--green-light) 100%);
  }
  .back-tagline {
    position: absolute;
    left: 44px;
    top: 154px;
    font-size: 27px;
    font-weight: 700;
    color: var(--card-white);
  }
  .back-mark {
    position: absolute;
    left: 348px;
    top: 85px;
    width: 180px;
    height: 180px;
    border-radius: 50%;
    border: 16px solid var(--card-white);
  }
</style>
</head>
<body>
  <section class="card card-front">
    <div class="front-ring"></div>
    <p class="holder-name">Tobi Aranmo</p>
    <p class="holder-title">Director</p>
    <div class="brand-strip"></div>
    <div class="brand-mark"></div>
    <p class="brand-name">TKR ENERGY</p>
    <p class="tagline-band">Lets Do The Impossible!</p>
    <p class="contact">N7 4QT, London, United Kingdom<br>xxxx pelvorpower.co.uk, www.pelvorpower.co.uk</p>
  </section>

  <section class="card card-back" role="img" aria-label="Green gradient with a repeating pattern of the brand symbol">
    <p class="back-tagline">Lets Do The Impossible!</p>
    <div class="back-mark"></div>
  </section>
</body>
</html>
```